www.BrightCoveSmileStudio.com needs to be re-designed

Current website to be redesigned www.BrightCoveSmileStudio.com

*Need a custom-made new theme

I need all 10 pages redesigned using existing content.
I need the website to be revamped to a more modern look.

Please start with Homepage first then after homepage mock up is approved we can move forward with rest of pages.

Please use existing images from my Facebook or Instagram page of our real customers for banner image...

(Where to find my FB and IG pages...
You can access these pages from the website header and "contact us" page for address.)

I would like to have a button that says "Book Appointment Online" and get rid of the actual form that is on current website.

But other than that please include all other content, features, etc in mock ups so I can make a decision on the website.

I prefer custom design and must be WP installable responsive theme.

This is design-only. I am open to any concepts you can submit.

Target Market(s)

people that care about thier looks

Industry/Entity Type

Dental Clinic

Colors

Designer to choose colors to be used in the design.

Requirements
Must have
• All current content/text that is currently on website. Just formatted so it doesnt look so busy. I want to make emphasis on BOOK APPOINTMENT button and $99 SPECIAL BUTTON
Nice to have
• White background so everything pops
Should not have
• I do not like stock photo images, please use images from my facebook and IG page of real customers or even a snap shot of our office building. You can access these pages from the website header and contact us page for address, maybe yu can use snapshot somewhere of building of our address on homepage possibly in banner image.

```html
<!DOCTYPE html>
<html lang="en">
<head>
<meta charset="utf-8">
<title>Bright Cove Smile Studio — Home</title>
<link rel="stylesheet" href="https://fonts.googleapis.com/css2?family=Roboto:wght@300;400;500;700&family=Allura&display=swap">
<style>
:root{
  --blue:#3fb4d2;
  --blue-dark:#2a9dbb;
  --orange:#f7931e;
  --red:#d61f1f;
  --ink:#222;
  --text:#555;
  --muted:#888;
  --grey-band:#5f5f5f;
  --light:#f3f3f3;
  --footer:#2a2a2a;
  --white:#fff;
}
*{box-sizing:border-box;margin:0;padding:0}
html,body{width:1200px;height:3285px;overflow:hidden;background:var(--white)}
body{font-family:'Roboto',sans-serif;color:var(--text);position:relative}
.abs{position:absolute}
.photo{position:absolute}

/* header */
.site-header{position:absolute;top:0;left:0;width:1200px;height:100px}
.brand{position:absolute;left:110px;top:26px;display:flex;align-items:center;gap:12px}
.brand-dot{width:48px;height:48px;border-radius:50%;background:#e6e6e6}
.brand-name{font-family:'Roboto',sans-serif;font-weight:500;font-size:20px;color:#4b4b4b;line-height:1.1}
.info{position:absolute;top:24px;display:flex;gap:12px;align-items:flex-start}
.info-tab{width:24px;height:54px;background:var(--blue);border-radius:0 27px 27px 0}
.info h4{font-size:14px;font-weight:500;color:var(--ink);margin-bottom:4px}
.info p{font-size:11.5px;color:var(--muted);line-height:1.45}
.info .big{font-size:15px;font-weight:700;color:#333}

.main-nav{position:absolute;top:105px;left:110px;height:48px;display:flex}
.main-nav a{font-size:14px;color:#444;text-decoration:none;padding:0 13px;line-height:48px}
.main-nav a.active{background:var(--blue);color:#fff;font-weight:500}

/* hero */
.hero{position:absolute;top:153px;left:0;width:1200px;height:515px;background:linear-gradient(90deg,#f4f4f4,#e9e9e9 60%,#dcdcdc)}
.hero-photo{left:840px;top:0;width:360px;height:515px;background:radial-gradient(ellipse at 55% 45%,#e8c9ae,#caa084 45%,#a77b55 75%,#d9d2c9)}
.hero h1{position:absolute;left:145px;top:80px;font-weight:500;font-size:44px;color:#1f1f1f;line-height:1.15;text-align:right;width:520px}
.hero h1 .script{font-family:'Allura',cursive;font-weight:400;font-size:74px;color:var(--blue)}
.call-band{position:absolute;left:0;top:236px;width:810px;height:22px;background:var(--blue);color:#fff;font-size:15px;letter-spacing:1.5px;font-weight:500;text-align:center;line-height:22px}
.hero-phone{position:absolute;left:0;width:810px;top:270px;text-align:center;font-size:40px;font-weight:300;color:#333}
.perks{position:absolute;top:385px;left:125px;display:flex;gap:48px}
.perk{display:flex;align-items:center;gap:14px;font-size:13.5px;color:#333;line-height:1.3}
.perk-icon{width:56px;height:56px;border-radius:50%;background:#fff;border:1px solid #ddd;display:flex;align-items:center;justify-content:center}

/* deal bar */
.deal-bar{position:absolute;left:0;width:1200px;height:68px;display:flex}
.deal-main{width:810px;background:var(--orange);color:#fff;display:flex;align-items:center;padding-left:110px;font-size:21px;font-weight:500;gap:8px}
.deal-main .price{font-size:50px;font-weight:700;line-height:1}
.deal-main .price sup{font-size:22px}
.deal-main .reg{font-weight:400}
.deal-cta{flex:1;background:var(--red);color:#fff;font-size:14px;font-weight:500;display:flex;align-items:center;padding-left:50px;position:relative;gap:8px}
.deal-cta::before{content:"";position:absolute;left:-1px;top:0;border-top:34px solid transparent;border-bottom:34px solid transparent;border-left:22px solid var(--orange)}

/* intro */
.intro{position:absolute;top:736px;left:0;width:1200px;height:380px}
.intro h2{position:absolute;left:110px;top:50px;font-size:20px;font-weight:500;color:var(--ink)}
.intro .lead{position:absolute;left:110px;top:80px;font-size:14px;font-weight:700;color:var(--blue)}
.intro .copy{position:absolute;left:110px;top:115px;width:460px;font-size:12.5px;line-height:1.6}
.intro .copy p{margin-bottom:16px}
.video{position:absolute;left:620px;top:58px;width:468px;height:268px;background:linear-gradient(#f2f2f2,#dcdcdc);box-shadow:0 0 0 1px #ddd}
.video-name{position:absolute;left:0;right:0;top:110px;text-align:center;font-size:26px;color:#555;font-weight:500}
.play{position:absolute;left:212px;top:113px;width:46px;height:34px;border-radius:9px;background:var(--red)}
.play::after{content:"";position:absolute;left:18px;top:10px;border-top:7px solid transparent;border-bottom:7px solid transparent;border-left:12px solid #fff}

/* how it works */
.how{position:absolute;top:1117px;left:0;width:1200px;height:515px;background:var(--light)}
.team-photo{left:0;top:0;width:587px;height:515px;background:linear-gradient(135deg,#f6f6f6,#e2dcdc 50%,#9a5a6b 80%,#7b3f52)}
.how-accent{position:absolute;left:520px;top:0;width:67px;height:70px;background:var(--blue);border-radius:0 0 0 67px}
.how h2{position:absolute;left:612px;top:52px;font-size:18px;font-weight:500;color:var(--ink)}
.how .copy{position:absolute;left:612px;top:85px;width:480px;font-size:12.3px;line-height:1.6}
.how .copy p{margin-bottom:16px}
.strip{position:absolute;top:1632px;left:0;width:1200px;height:138px;display:flex}
.strip div{flex:1}

/* blog + testimonials */
.split-head{position:absolute;top:1770px;left:0;width:1200px;height:125px;display:flex}
.split-head div{flex:1;display:flex;align-items:center;justify-content:center;gap:12px;color:#fff;font-size:20px;font-weight:500}
.split-head .blue{background:var(--blue)}
.split-head .grey{background:var(--grey-band)}
.mid-badge{position:absolute;left:558px;top:1790px;width:84px;height:84px;border-radius:50%;background:#fff;box-shadow:0 0 0 4px rgba(255,255,255,.5)}
.split-body{position:absolute;top:1895px;left:0;width:1200px;height:383px}
.divider{position:absolute;left:600px;top:0;width:1px;height:383px;background:#e2e2e2}
.post{position:absolute;left:110px;display:flex;gap:25px}
.post-thumb{width:142px;height:118px}
.post h3{font-size:14px;font-weight:500;color:var(--ink);margin-bottom:6px}
.post .meta{font-size:10.5px;color:var(--muted);margin-bottom:14px}
.post .meta b{color:var(--blue);font-weight:400}
.post p{font-size:12.5px;line-height:1.55;width:250px}
.more{display:inline-block;width:10px;height:10px;border-radius:50%;background:var(--blue);vertical-align:middle}
.quote{position:absolute;left:630px;display:flex;gap:28px}
.avatar{width:84px;height:84px;border-radius:50%}
.quote p{font-size:12.5px;line-height:1.55;width:400px;margin-top:6px}
.quote .who{margin-top:14px;font-size:13px;color:var(--ink)}
.quote .where{font-size:11.5px;color:var(--muted);padding-left:12px}

/* compare */
.compare{position:absolute;top:2278px;left:0;width:1200px;height:438px;background:linear-gradient(90deg,#eef2e6,#e3e9d8 45%,#eef0ea)}
.compare-photo{left:940px;top:0;width:260px;height:340px;background:radial-gradient(ellipse at 40% 40%,#d6ad8e,#a9795b 55%,#e6e2da 85%)}
.compare h2{position:absolute;left:110px;top:50px;font-size:18px;font-weight:500;color:var(--ink)}
table.compare-table{position:absolute;left:116px;top:116px;width:964px;border-collapse:collapse;background:#fff;box-shadow:0 2px 6px rgba(0,0,0,.15);font-size:12px;text-align:center}
.compare-table th{height:70px;background:var(--blue);color:#fff;font-size:18px;font-weight:500;border-right:2px solid #fff}
.compare-table th.label{background:#555;width:192px}
.compare-table td{height:44px;border-bottom:1px solid #e4e4e4;color:#555}
.compare-table td.label{background:#ebebeb;font-weight:500;color:#333}
.compare-table tr.cost td{height:58px;background:#dcebf1;font-size:17px;font-weight:700;color:#222}
.compare-table tr.cost td.label{background:#e0e0e0;font-size:13px;font-weight:500}
.compare-table td.ours{background:#f7f7f7}

/* why */
.why h2{position:absolute;top:2775px;left:0;width:1200px;text-align:center;font-size:19px;font-weight:500;color:var(--ink)}
.reasons{position:absolute;top:2835px;left:110px;width:980px;display:flex;justify-content:space-between}
.reason{width:182px;height:62px;border-radius:31px;background:var(--blue);display:flex;align-items:center;gap:16px;padding-left:6px;color:#fff;font-size:15px;font-weight:500}
.reason-icon{width:50px;height:50px;border-radius:50%;background:#fff;display:flex;align-items:center;justify-content:center}

/* footer */
.site-footer{position:absolute;top:3027px;left:0;width:1200px;height:258px;background:var(--footer);color:#aaa}
.foot-badge{position:absolute;left:110px;top:40px;width:100px;height:100px;border-radius:50%;background:#fff}
.site-footer h5{position:absolute;top:30px;color:#fff;font-size:13px;font-weight:500;letter-spacing:.5px}
.links{position:absolute;left:278px;top:70px;display:grid;grid-template-columns:140px 140px;row-gap:6px;font-size:12px}
.contact{position:absolute;left:582px;top:70px;font-size:12px;line-height:1.6}
.newsletter input{position:absolute;left:866px;top:70px;width:220px;height:36px;border-radius:18px;border:0;padding-left:16px;font-family:inherit;font-size:12px}
.newsletter button{position:absolute;left:866px;top:120px;width:110px;height:32px;border-radius:16px;border:0;background:var(--blue);color:#fff;font-family:inherit;font-weight:700;font-size:11px}
.legal{position:absolute;left:110px;top:206px;font-size:11.5px}
.socials{position:absolute;left:906px;top:196px;display:flex;gap:8px}
.socials span{width:28px;height:28px;border-radius:50%;border:1px solid #777}
</style>
</head>
<body>

<header class="site-header">
  <div class="brand"><span class="brand-dot"></span><span class="brand-name">Bright Cove<br>Smile Studio</span></div>
  <div class="info" style="left:430px">
    <span class="info-tab"></span>
    <div><h4>Book Appointment</h4><p>Mon-Fri : 8:30am to 5:00pm<br>Sat-Sun : Closed</p></div>
  </div>
  <div class="info" style="left:662px">
    <span class="info-tab"></span>
    <div><h4>Clinic Hours</h4><p>Mon-Fri : 9:15am to 5:30pm<br>Sat : 10am to 2pm (Sun: Closed)</p></div>
  </div>
  <div class="info" style="left:913px">
    <span class="info-tab"></span>
    <div><p>Bright Cove Smile Studio<br>Call Now! Today</p><p class="big">555-214-7730</p></div>
  </div>
</header>

<nav class="main-nav">
  <a class="active">Home</a><a>Our Process</a><a>Photos</a><a>White Smile Club</a><a>Testimonials</a><a>Appointments</a><a>FAQ</a><a>Contact Us</a><a>Blog</a><a>Buy Now</a>
</nav>

<section class="hero">
  <div class="photo hero-photo" role="img" aria-label="Smiling customer with freshly whitened teeth"></div>
  <h1>Get That <span class="script">White Smile</span><br>You've Always Wanted</h1>
  <div class="call-band">GIVE US A CALL TO SCHEDULE AN APPOINTMENT</div>
  <div class="hero-phone">555-214-7730</div>
  <div class="perks">
    <div class="perk"><span class="perk-icon"><svg width="26" height="26" viewBox="0 0 26 26" fill="none" stroke="#3fb4d2" stroke-width="1.6"><path d="M6 5c3-2 5 0 7 0s4-2 7 0c2 2 1 6-1 9l-2 9-2-6h-4l-2 6-2-9C5 11 4 7 6 5z"/></svg></span><span>Amazing<br>Results</span></div>
    <div class="perk"><span class="perk-icon"><svg width="26" height="26" viewBox="0 0 26 26" fill="none" stroke="#3fb4d2" stroke-width="1.6"><rect x="5" y="7" width="16" height="14" rx="2"/><path d="M9 14l3 3 5-6"/></svg></span><span>The Most<br>Effective System</span></div>
    <div class="perk"><span class="perk-icon"><svg width="26" height="26" viewBox="0 0 26 26" fill="none" stroke="#3fb4d2" stroke-width="1.6"><path d="M4 12c4 3 14 3 18 0M4 12c2 6 16 6 18 0"/></svg></span><span>More Affordable<br>Than The Dentist</span></div>
  </div>
</section>

<div class="deal-bar" style="top:668px">
  <div class="deal-main">Click Here To Get Our <span class="price"><sup>$</sup>99</span> Teeth Whitening Deal <span class="reg">(Reg $378)</span></div>
  <div class="deal-cta">Book Appointment Online Now! <svg width="14" height="14" viewBox="0 0 14 14"><circle cx="7" cy="7" r="7" fill="#fff"/><path d="M5.5 4l3 3-3 3" stroke="#d61f1f" stroke-width="1.8" fill="none"/></svg></div>
</div>

<section class="intro">
  <h2>Bright Cove Smile Studio</h2>
  <div class="lead">The best price, service and results.</div>
  <div class="copy">
    <p>Bright Cove Smile Studio features state-of-the-art technologies that are safe, industry-unique and very cost-effective. Our teeth whitening system utilizes the latest blue light whitening technology. Our Blue Light Systems are calibrated precisely for optimal activation of our exclusive hydrogen peroxide based whitening solution which is manufactured in a FDA registered facility in the USA.</p>
    <p>Our special lighting systems intensify the release of hydroxyl radicals that accelerate the dissipation of tooth stains. The entire teeth whitening process is accelerated and able to be completed in just 45 minutes with instant results.</p>
  </div>
  <div class="video" role="img" aria-label="Studio introduction video">
    <div class="video-name">Bright Cove Smile Studio</div>
    <span class="play"></span>
  </div>
</section>

<section class="how">
  <div class="photo team-photo" role="img" aria-label="Studio team with a happy customer holding a sign"></div>
  <span class="how-accent"></span>
  <h2>How It Works</h2>
  <div class="copy">
    <p>We have a very effective teeth whitening treatment that is guaranteed to get you quick results in about 1 hour. To start the treatment you'll apply a Hydrogen Peroxide based whitening agent to your teeth. We then place our cold blue light directly in front of your exposed teeth for 15 minutes per treatment. The lighting systems we use activate the whitening agent and thats what accelerates the whitening process, giving you whiter teeth in less than an hour.</p>
    <p>We always perform what we call a "Triple Treatment". So that's 3 of the 15 minute treatments all done consecutively, in the same visit. The actual whitening time is a total of 45 minutes. Now there is a few minute break in between each 15 minute treatment and this is why we tell all of our patients to give yourself one hour at the office. The biggest benefit of doing an in office treatment vs a take home kit is that you will see results immediately after the treatment. We also include our home maintenance kit for after care. It's very important that no matter where you get your teeth whitened, you need to maintain them for long lasting results. You'll use our maintenance kit once or twice per month as a touch up to help maintain your newly whitened teeth, and that ultimately make your results last longer.</p>
  </div>
</section>

<div class="strip" role="img" aria-label="Photos of the studio and customers during treatment">
  <div style="background:linear-gradient(#d9d4cf,#9c918a)"></div>
  <div style="background:linear-gradient(#c9b3a2,#7d6457)"></div>
  <div style="background:linear-gradient(#d8c3b3,#8e6e5d)"></div>
  <div style="background:linear-gradient(#e0d2c8,#a58a7a)"></div>
  <div style="background:linear-gradient(#c7c9de,#6f6aa8)"></div>
</div>

<div class="split-head">
  <div class="blue"><svg width="24" height="20" viewBox="0 0 24 20" fill="none" stroke="#fff" stroke-width="1.8"><path d="M2 7h5l9-5v16l-9-5H2z"/></svg>From The Blog</div>
  <div class="grey"><svg width="24" height="20" viewBox="0 0 24 20" fill="none" stroke="#fff" stroke-width="1.8"><path d="M2 2h20v12H8l-5 4V2z"/></svg>Testimonials</div>
</div>
<span class="mid-badge"></span>

<section class="split-body">
  <span class="divider"></span>
  <article class="post" style="top:42px">
    <div class="post-thumb" role="img" aria-label="Toothbrushes in a cup" style="background:linear-gradient(135deg,#b53b3b,#3d6ea8 60%,#e7d27a)"></div>
    <div><h3>When to stop brushing your kids teeth</h3><div class="meta">by <b>Nadia</b> | 08 May 2017 | 0 Comment</div><p>Lorem Ipsum is simply dummy text of the printing and typesetting industry. Lorem Ipsum type specimen book. <span class="more"></span></p></div>
  </article>
  <article class="post" style="top:212px">
    <div class="post-thumb" role="img" aria-label="Close-up of a bright smile" style="background:linear-gradient(#c96a6a,#f1e7e0 50%,#b45757)"></div>
    <div><h3>Can you reverse the effects of a cavity?</h3><div class="meta">by <b>Nadia</b> | 08 May 2017 | 0 Comment</div><p>Lorem Ipsum is simply dummy text of the printing and typesetting industry. Lorem Ipsum type specimen book. <span class="more"></span></p></div>
  </article>
  <div class="quote" style="top:42px">
    <div class="avatar" role="img" aria-label="Customer portrait" style="background:radial-gradient(#c89c80,#6a4a3c)"></div>
    <div><p>"This is Marco, yesterday I had my whitening in your clinic , and I am so happy with my teeth. I appreciate your service and thank you."</p><div class="who">- Marco Y.</div><div class="where">Bright Cove, CA</div></div>
  </div>
  <div class="quote" style="top:212px">
    <div class="avatar" role="img" aria-label="Customer portrait" style="background:radial-gradient(#e2b48e,#b0602e)"></div>
    <div><p>"Great price, great results, easy and painless. This place was easy to find. The price was outstanding! And my teeth are at least two shades!"</p><div class="who">- Elena K.</div><div class="where">Bright Cove, CA</div></div>
  </div>
</section>

<section class="compare">
  <div class="photo compare-photo" role="img" aria-label="Smiling woman"></div>
  <h2>Compare Us</h2>
  <table class="compare-table">
    <tr><th class="label">Features</th><th>Lamp Pro</th><th>Bright Cove</th><th>Glow Strips</th><th>Home Kits</th></tr>
    <tr class="cost"><td class="label">Cost</td><td>$300-$600</td><td>$378</td><td>$300-$600</td><td>$50-$150</td></tr>
    <tr><td class="label">Speed</td><td>1-2 Hours</td><td class="ours">45 Mins</td><td>7-14 Days</td><td>7-30 Days</td></tr>
    <tr><td class="label">Ease Of Use</td><td>Difficult/Dentist</td><td class="ours">Very Easy</td><td>Difficult</td><td>Difficult</td></tr>
    <tr><td class="label">Availability</td><td>Limited Availability</td><td class="ours">Appt Only</td><td>Limited Availability</td><td>Store Purchase</td></tr>
    <tr><td class="label">Pain</td><td>Pain &amp; Sensitivity</td><td class="ours">No Pain</td><td>Sensitivity</td><td>Sensitivity</td></tr>
  </table>
</section>

<section class="why">
  <h2>Why Choose Us?</h2>
  <div class="reasons">
    <div class="reason"><span class="reason-icon"><svg width="26" height="26" viewBox="0 0 26 26" fill="none" stroke="#3fb4d2" stroke-width="1.8"><circle cx="13" cy="13" r="10"/><path d="M16 9h-4a2 2 0 000 4h2a2 2 0 010 4h-4M13 7v12"/></svg></span>Price</div>
    <div class="reason"><span class="reason-icon"><svg width="26" height="26" viewBox="0 0 26 26" fill="none" stroke="#3fb4d2" stroke-width="1.8"><rect x="4" y="4" width="18" height="18" rx="2"/><path d="M7 18l5-5 3 3 5-6"/></svg></span>Results</div>
    <div class="reason"><span class="reason-icon"><svg width="26" height="26" viewBox="0 0 26 26" fill="none" stroke="#3fb4d2" stroke-width="1.8"><circle cx="13" cy="13" r="10"/><path d="M6 6l14 14"/></svg></span>No Pain</div>
    <div class="reason"><span class="reason-icon"><svg width="26" height="26" viewBox="0 0 26 26" fill="none" stroke="#3fb4d2" stroke-width="1.8"><circle cx="13" cy="13" r="4"/><path d="M13 3v4M13 19v4M3 13h4M19 13h4M6 6l3 3M17 17l3 3M20 6l-3 3M9 17l-3 3"/></svg></span>Service</div>
    <div class="reason"><span class="reason-icon"><svg width="26" height="26" viewBox="0 0 26 26" fill="none" stroke="#3fb4d2" stroke-width="1.8"><path d="M5 18c0-7 5-11 13-11M14 3l4 4-4 4"/></svg></span>Convenience</div>
  </div>
</section>

<div class="deal-bar" style="top:2958px">
  <div class="deal-main">Click Here To Get Our <span class="price"><sup>$</sup>99</span> Teeth Whitening Deal <span class="reg">(Reg $378)</span></div>
  <div class="deal-cta">Book Appointment Online Now! <svg width="14" height="14" viewBox="0 0 14 14"><circle cx="7" cy="7" r="7" fill="#fff"/><path d="M5.5 4l3 3-3 3" stroke="#d61f1f" stroke-width="1.8" fill="none"/></svg></div>
</div>

<footer class="site-footer">
  <span class="foot-badge"></span>
  <h5 style="left:278px">QUICK LINKS</h5>
  <div class="links"><span>Home</span><span>Appointments</span><span>Our Process</span><span>FAQ</span><span>Photos</span><span>Contact</span><span>White Smile Club</span><span>Blog</span><span>Testimonials</span><span>Buy Now</span></div>
  <h5 style="left:582px">CONTACT INFO</h5>
  <div class="contact">1480 Harbor View Drive Ste 210,<br>Bright Cove, CA 90410<br><br>T: 555-301-4482<br>T: 800-555-0196</div>
  <h5 style="left:866px">SUBSCRIBE NEWSLETTER</h5>
  <div class="newsletter"><input type="text" placeholder="Name"><button>SUBSCRIBE</button></div>
  <div class="legal">© 2017 Bright Cove Smile Studio. Terms of Use | Privacy | Sitemap</div>
  <div class="socials"><span></span><span></span><span></span><span></span><span></span><span></span></div>
</footer>

</body>
</html>
```